Its just a copy of my concept with little changes.
Be careful you have to come with your unique concept.
All - I'm not sure how some of you are using a prior generation of my logo design, but in the final design (which I did upload for this project), the words in the tagline are flipped so Insight appears first. Please be sure you are using proper version. Thanks! Dot
All - I think the fax number should immediately follow the phone as the numbers are consecutive. Please do not include the cell phone on the letterhead, just on the business card. Appeals, Commercial Litigation (my practice areas) needs to be specified on both. Thanks!
Please note this is a combined project with Hallbrook Law Branding. I'm working with tech support to change the project names so it's clear this is a package. Thanks!
Thanks for all your great work and creativity! This is going to be a hard decison.
Dot

```html
<!DOCTYPE html>
<html lang="en">
<head>
<meta charset="utf-8">
<title>Hallbrook Law — Stationery</title>
<link href="https://fonts.googleapis.com/css2?family=Open+Sans:wght@400;600;700&display=swap" rel="stylesheet">
<style>
  :root{
    --gold-dark:#b8955a;
    --gold:#cdb07a;
    --gold-light:#ebdcbc;
    --gold-faint:#f6efe2;
    --ink:#7a5a2a;
    --text:#6e6252;
    --paper:#ffffff;
    --edge:#e2dccf;
  }
  *{box-sizing:border-box;margin:0;padding:0}
  html,body{width:1200px;height:826px;overflow:hidden;background:var(--paper)}
  body{position:relative;font-family:"Open Sans",Arial,sans-serif;color:var(--text)}

  .sheet{position:absolute;background:var(--paper);border:1px solid var(--edge);box-shadow:0 1px 4px rgba(0,0,0,.12);overflow:hidden}
  .band-top{position:absolute;left:0;top:0;right:0;background:linear-gradient(90deg,var(--gold-dark),var(--gold) 40%,var(--gold-light))}
  .band-left{position:absolute;left:0;top:0;bottom:0;background:linear-gradient(180deg,var(--gold-dark),var(--gold) 55%,var(--gold-light))}
  .pattern-area{position:absolute;background:linear-gradient(180deg,var(--gold-faint),rgba(246,239,226,0))}

  .brand{position:absolute;display:flex;align-items:flex-start;gap:8px}
  .brand-square{width:22px;height:22px;background:var(--gold);flex:none;margin-top:2px}
  .brand-name{font-weight:600;color:var(--ink);text-transform:uppercase;line-height:1.15;letter-spacing:.03em}
  .tagline{font-size:8px;color:var(--ink);margin-top:3px;letter-spacing:.02em;text-transform:none}

  /* Letterhead */
  .letterhead{left:19px;top:19px;width:610px;height:787px}
  .letterhead .band-top{height:16px}
  .letterhead .band-left{width:17px}
  .letterhead .pattern-area{left:197px;top:341px;width:384px;height:380px}
  .letterhead .brand{left:36px;top:34px}
  .letterhead .brand-name{font-size:13px}
  .practice{position:absolute;font-weight:700;color:var(--ink)}
  .letterhead .practice{left:36px;bottom:16px;font-size:11px}
  .contact{position:absolute;text-align:right;font-size:9px;line-height:1.45;color:var(--text)}
  .letterhead .contact{right:22px;bottom:16px}

  /* Envelope */
  .envelope{left:509px;top:96px;width:650px;height:293px}
  .envelope .band-top{height:12px}
  .envelope .band-left{width:12px}
  .envelope .pattern-area{left:439px;top:60px;width:204px;height:226px}
  .envelope .brand{left:30px;top:24px}
  .envelope .brand-name{font-size:13px}
  .envelope .return-address{position:absolute;left:30px;bottom:16px;font-size:9px;color:var(--ink)}

  /* Business card */
  .card{left:730px;top:499px;width:446px;height:144px}
  .card .band-top{height:10px}
  .card .band-left{width:9px}
  .card .pattern-area{left:316px;top:22px;width:124px;height:118px}
  .card .brand{left:22px;top:16px}
  .card .brand-square{width:18px;height:18px}
  .card .brand-name{font-size:10px}
  .card .tagline{font-size:6.5px}
  .card-person{position:absolute;left:22px;top:64px}
  .person-name{font-size:9.5px;font-weight:700;color:var(--ink)}
  .person-role{font-size:7px;color:var(--text)}
  .card .contact{left:22px;top:98px;right:auto;text-align:left;font-size:6.5px;line-height:1.5}
</style>
</head>
<body>

<section class="sheet letterhead">
  <div class="band-top"></div>
  <div class="band-left"></div>
  <div class="pattern-area" role="img" aria-label="Faint gold Greek key pattern watermark"></div>
  <div class="brand">
    <span class="brand-square"></span>
    <div class="brand-name">Law Office of<br>Dorothy B Hallbrook
      <div class="tagline">Clarity ... Counsel ... Commitment</div>
    </div>
  </div>
  <p class="practice">Appeals -- Commercial Litigation</p>
  <div class="contact">
    1180 W. Cedar Ridge Road, Tolleson, Arizona 85353-0410<br>
    Phone: 623-555-0142 • Fax: 623-555-0143<br>
    Email: dot@hallbrooklaw.com • www.hallbrooklaw.com
  </div>
</section>

<section class="sheet envelope">
  <div class="band-top"></div>
  <div class="band-left"></div>
  <div class="pattern-area" role="img" aria-label="Faint gold Greek key pattern watermark"></div>
  <div class="brand">
    <span class="brand-square"></span>
    <div class="brand-name">Law Office of<br>Dorothy B Hallbrook
      <div class="tagline">Clarity ... Counsel ... Commitment</div>
    </div>
  </div>
  <p class="return-address">1180 W. Cedar Ridge Road, Tolleson, Arizona 85353-0410</p>
</section>

<section class="sheet card">
  <div class="band-top"></div>
  <div class="band-left"></div>
  <div class="pattern-area" role="img" aria-label="Faint gold Greek key pattern watermark"></div>
  <div class="brand">
    <span class="brand-square"></span>
    <div class="brand-name">Law Office of<br>Dorothy B Hallbrook
      <div class="tagline">Clarity ... Counsel ... Commitment</div>
    </div>
  </div>
  <div class="card-person">
    <p class="person-name">Dot Hallbrook</p>
    <p class="person-role">Appeals -- Commercial Litigation</p>
  </div>
  <div class="contact">
    1180 W. Cedar Ridge Road, Tolleson, Arizona 85353-0410<br>
    Phone: 623-555-0142 • Fax: 623-555-0143 • Cell: 623-555-0199<br>
    Email: dot@hallbrooklaw.com • www.hallbrooklaw.com
  </div>
</section>

</body>
</html>
```